Business acrd and Stationery desgin FOR HARLOW

I want creative and expressive stationary design .on the front side for business card I need the logo and doctors name to be there and on the back side I need time and appointment .Please see attached business card to use same names ,but use address below and phone number

Note:the deigner must submit the file in vector format and PSD and PDF

Business name is :Harlow Crest Medical Clinic.

Address:
20485 57 ST NW
City :EDMONTON AB
Postal code: T6K 3P8

Phone :(780) 492-3815
Fax:(780) 492-5127

Other Business name :Harlow Medical Clinic

• logo in the back on business card

```html
<!DOCTYPE html>
<html lang="en">
<head>
<meta charset="utf-8">
<title>Harlow Crest Medical Clinic – Letterhead</title>
<link rel="stylesheet" href="https://fonts.googleapis.com/css2?family=Questrial&display=swap">
<style>
  :root {
    --backdrop: #ececec;
    --paper: #ffffff;
    --brand-red: #d7232f;
    --brand-navy: #2b3f92;
    --ink: #3a3a3a;
    --ink-soft: #6a6a6a;
    --signature-tone: #dfe3f1;
  }
  * { box-sizing: border-box; margin: 0; padding: 0; }
  html, body {
    width: 1200px; height: 934px; overflow: hidden;
    background: var(--backdrop);
    font-family: "Questrial", "Century Gothic", sans-serif;
    color: var(--ink);
  }
  .letterhead {
    position: absolute; left: 300px; top: 43px;
    width: 600px; height: 848px;
    background: var(--paper);
    border-top: 5px solid var(--brand-red);
    border-bottom: 9px solid var(--brand-navy);
    box-shadow: 0 4px 18px rgba(0,0,0,.12);
  }
  .brand {
    position: absolute; left: 48px; top: 120px;
    display: flex; align-items: center; gap: 8px;
  }
  .brand-dot {
    width: 14px; height: 14px; border-radius: 50%;
    background: var(--brand-red);
  }
  .brand-name {
    font-size: 15px; color: var(--brand-navy);
    letter-spacing: .3px; text-transform: uppercase;
  }
  .contact {
    position: absolute; right: 48px; top: 58px;
    display: flex; gap: 18px;
    font-size: 7.5px; line-height: 1.55; color: var(--ink-soft);
  }
  .contact-line { display: flex; align-items: center; gap: 4px; }
  .contact-icon {
    width: 8px; height: 8px; border-radius: 1.5px;
    background: var(--brand-red);
    display: inline-flex; align-items: center; justify-content: center;
  }
  .recipient {
    position: absolute; left: 48px; top: 200px;
    font-size: 8px; line-height: 1.5; color: var(--ink-soft);
  }
  .letter-body {
    position: absolute; left: 48px; top: 272px; width: 500px;
    font-size: 8.3px; line-height: 1.5; color: var(--ink-soft);
  }
  .salutation { font-weight: 700; color: var(--ink); margin-bottom: 10px; }
  .letter-body p { margin-bottom: 10px; }
  .closing { margin-top: 14px; display: flex; align-items: flex-end; gap: 14px; }
  .closing-name { font-weight: 700; color: var(--ink); }
  .signature-area {
    width: 80px; height: 38px; border-radius: 4px;
    background: linear-gradient(135deg, var(--signature-tone), #f1f3f9);
  }
</style>
</head>
<body>
  <main class="letterhead">
    <div class="brand">
      <span class="brand-dot"></span>
      <span class="brand-name">Harlow Crest Medical Clinic</span>
    </div>

    <address class="contact" style="font-style:normal">
      <div>
        <div>20485 57 ST NW</div>
        <div>Edmonton AB, T6K 3P8</div>
      </div>
      <div>
        <div class="contact-line">
          <span class="contact-icon">
            <svg width="6" height="6" viewBox="0 0 10 10"><path d="M2 1l2 2-1 1.5c.8 1.4 1.6 2.2 3 3L7.5 6.5l2 2L8 10C4 9.5.5 6 0 2z" fill="#fff"/></svg>
          </span>(780) 492-3815
        </div>
        <div class="contact-line">
          <span class="contact-icon">
            <svg width="6" height="6" viewBox="0 0 10 10"><rect x="1" y="3" width="8" height="5" fill="#fff"/><rect x="3" y="1" width="4" height="2" fill="#fff"/></svg>
          </span>(780) 492-5127
        </div>
      </div>
    </address>

    <div class="recipient">
      <div>30.02.2015</div>
      <div>Recipient's name</div>
      <div>Lindenweg 14</div>
      <div>10115 Berlin</div>
      <div>Germany</div>
    </div>

    <section class="letter-body">
      <div class="salutation">Dear sir,</div>
      <p>Communication is a vital part of everyday life for people and organisations alike. It may be spoken or written, and written words remain when spoken ones fade. Today we reach one another through telephones, email, video calls and messages, yet letters still hold a place of their own.</p>
      <p>In a world of rapid invention, many ways of writing have become faster and cheaper. Still, a printed letter carries weight that a short message cannot, and many offices continue to rely on it for records, notices and formal replies that must be kept.</p>
      <p>A letter speaks for the person or clinic that sends it, so the wording should be clear, polite and suited to its purpose. Take care with every detail before it is signed.</p>
      <p>Writing a good letter is a skill. The samples we keep give a useful starting point, and each one can be shaped to fit the occasion and the reader.</p>
      <div class="closing">
        <div>
          <div>Yours Sincerely,</div>
          <div class="closing-name">Tessa Morlin</div>
        </div>
        <div class="signature-area" role="img" aria-label="Handwritten signature"></div>
      </div>
    </section>
  </main>
</body>
</html>
```